sign to promote finished job on new houses

I would like the sign to say.

Garage door by,
Wombat creek garage doors
Ph Darren
0415863027
Dar3811@mailbox-example.net
Updates

Project Deadline Extended Reason: I have a logo being designed and will post here to incorporate into a flyer. Please people, don't waste anymore of your time for the moment. My apologies Will post asap Added Wednesday, September 2, 2015

Target Market(s)

New customers

Industry/Entity Type

Garage

Requirements
Must have
• Clear text
Nice to have
• A sign

```html
<!DOCTYPE html>
<html lang="en">
<head>
<meta charset="utf-8">
<title>Wombat Creek Garage Doors – Services Flyer</title>
<link href="https://fonts.googleapis.com/css2?family=Oswald:wght@400;500;700&family=Open+Sans:wght@400;600&display=swap" rel="stylesheet">
<style>
  :root {
    --orange: #f28a1c;
    --orange-deep: #e06a12;
    --orange-light: #f7a441;
    --red: #e02b20;
    --red-dark: #b81d15;
    --charcoal: #3a3330;
    --white: #ffffff;
    --cream: #fbeee2;
    --foliage: #5c6b45;
    --roof: #45464a;
    --wall: #b8a27e;
    --door: #7a5a42;
    --door-dark: #5e4432;
  }
  * { margin: 0; padding: 0; box-sizing: border-box; }
  html, body { width: 851px; height: 1200px; overflow: hidden; background: var(--white); }
  .flyer {
    position: relative;
    width: 851px; height: 1200px;
    overflow: hidden;
    font-family: "Open Sans", Arial, sans-serif;
    color: var(--white);
    background: var(--orange);
  }
  .hero-photo {
    position: absolute; left: 0; top: 0; width: 851px; height: 560px;
    background:
      linear-gradient(90deg, rgba(120,110,100,0.55) 0%, rgba(120,110,100,0) 12%, rgba(120,110,100,0) 88%, rgba(92,107,69,0.6) 100%),
      linear-gradient(180deg, var(--foliage) 0%, var(--roof) 9%, var(--roof) 24%, var(--wall) 30%, var(--wall) 40%, var(--door) 48%, var(--door-dark) 75%, var(--door) 100%);
  }
  .backdrop { position: absolute; left: 0; top: 0; width: 851px; height: 1200px; }
  .brand {
    position: absolute; left: 22px; top: 14px;
    width: 190px; height: 190px; border-radius: 50%;
    background: var(--red);
    display: flex; flex-direction: column; align-items: center; justify-content: center;
    text-align: center;
    font-family: "Oswald", Arial, sans-serif; font-weight: 500;
    color: var(--white); line-height: 1.1;
    text-transform: uppercase;
  }
  .brand .brand-by { font-size: 15px; letter-spacing: 1px; margin-bottom: 4px; }
  .brand .brand-name { font-size: 26px; letter-spacing: 0.5px; }
  .services {
    position: absolute; left: 30px; top: 560px; width: 410px;
  }
  .services h2 {
    font-family: "Oswald", Arial, sans-serif; font-weight: 400;
    font-size: 50px; letter-spacing: 1px; line-height: 1;
  }
  .services .intro { font-size: 20px; margin: 14px 0 12px; }
  .service-list { list-style: none; }
  .service-list li {
    font-size: 20px; line-height: 1.45;
    display: flex; align-items: center; gap: 14px;
  }
  .service-list svg { flex: none; }
  .job-photo {
    position: absolute; left: 455px; width: 370px; border: 5px solid var(--white);
  }
  .job-photo.modern { top: 565px; height: 180px; background: linear-gradient(180deg, #8fa3b8 0%, #6a6e74 35%, #2f3236 70%, #4a4d52 100%); }
  .job-photo.classic { top: 752px; height: 185px; background: linear-gradient(180deg, #6f6a64 0%, #5b5650 25%, #d8d2c2 45%, #cfc8b8 85%, #6d7a55 100%); }
  .remote-photo {
    position: absolute; left: 12px; top: 845px; width: 180px; height: 180px; border-radius: 50%;
    border: 6px solid var(--white);
    background: radial-gradient(circle at 40% 40%, #d9d4cf 0%, #9c948c 60%, #5a524c 100%);
  }
  .specialty {
    position: absolute; left: 160px; top: 965px; width: 370px; height: 112px;
  }
  .specialty svg { position: absolute; left: 0; top: 0; }
  .specialty .specialty-text { position: absolute; left: 60px; top: 14px; }
  .specialty h3 {
    font-family: "Oswald", Arial, sans-serif; font-weight: 400;
    font-size: 34px; letter-spacing: 1px; line-height: 1;
  }
  .specialty p { font-size: 17px; line-height: 1.25; margin-top: 6px; }
  .contact-bar {
    position: absolute; left: 0; top: 1100px; width: 851px; height: 100px;
    background: var(--charcoal);
  }
  .contact-name {
    position: absolute; left: 215px; top: 1092px; width: 225px; height: 108px;
    background: var(--orange-deep);
    font-family: "Oswald", Arial, sans-serif; font-weight: 700;
    font-size: 54px; display: flex; align-items: center; justify-content: center;
    letter-spacing: 1px;
  }
  .contact-details {
    position: absolute; left: 462px; top: 1118px;
    font-size: 19px; line-height: 1.4; color: var(--white);
  }
</style>
</head>
<body>
<div class="flyer">
  <div class="hero-photo" role="img" aria-label="Photograph of a stone-clad house front with a dark roof and a brown carriage-style garage door with windows"></div>

  <svg class="backdrop" width="851" height="1200" viewBox="0 0 851 1200" aria-hidden="true">
    <polygon points="0,500 851,470 851,1100 0,1100" fill="var(--orange)"/>
    <polygon points="0,500 520,485 300,560 0,560" fill="var(--orange-light)"/>
    <polygon points="560,480 851,470 851,540" fill="var(--orange-deep)"/>
    <polygon points="0,830 440,860 440,1100 0,1100" fill="var(--cream)"/>
    <polygon points="440,860 851,820 851,1100 440,1100" fill="var(--orange-deep)"/>
  </svg>

  <div class="brand">
    <span class="brand-by">Garage door by</span>
    <span class="brand-name">Wombat Creek<br>Garage Doors</span>
  </div>

  <section class="services">
    <h2>SERVICES</h2>
    <p class="intro">We provide the following services :</p>
    <ul class="service-list">
      <li><svg width="20" height="16" viewBox="0 0 20 16"><path d="M0 0 L20 8 L0 16 L5 8 Z" fill="var(--white)"/></svg>Build doors and gates</li>
      <li><svg width="20" height="16" viewBox="0 0 20 16"><path d="M0 0 L20 8 L0 16 L5 8 Z" fill="var(--white)"/></svg>New garage doors installation</li>
      <li><svg width="20" height="16" viewBox="0 0 20 16"><path d="M0 0 L20 8 L0 16 L5 8 Z" fill="var(--white)"/></svg>Remote openers</li>
      <li><svg width="20" height="16" viewBox="0 0 20 16"><path d="M0 0 L20 8 L0 16 L5 8 Z" fill="var(--white)"/></svg>Gate openers</li>
      <li><svg width="20" height="16" viewBox="0 0 20 16"><path d="M0 0 L20 8 L0 16 L5 8 Z" fill="var(--white)"/></svg>Maintenance &amp; Repair Work</li>
    </ul>
  </section>

  <div class="job-photo modern" role="img" aria-label="Photograph of a modern grey house with a black glass-panel garage door"></div>
  <div class="job-photo classic" role="img" aria-label="Photograph of a house with a cream panelled garage door"></div>

  <div class="remote-photo" role="img" aria-label="Photograph of a hand holding a garage door remote"></div>

  <div class="specialty">
    <svg width="370" height="112" viewBox="0 0 370 112" aria-hidden="true">
      <polygon points="30,0 370,0 340,112 0,112" fill="var(--red)"/>
      <polygon points="30,0 60,0 30,112 0,112" fill="var(--red-dark)"/>
    </svg>
    <div class="specialty-text">
      <h3>SPECIALIZING</h3>
      <p>in retro fitting remotes<br>to existing garage doors</p>
    </div>
  </div>

  <div class="contact-bar"></div>
  <div class="contact-name">DARREN</div>
  <div class="contact-details">
    Ph. 53-618-205 / 0415-863-027<br>
    Email. Dar3811@mailbox-example.net
  </div>
</div>
</body>
</html>
```